Business Card Design.

Life and Wellness Coach
www.brightpathwell.net
Want to use my name as the logo it could be the initials TRK or my full name. I want to trade mark me.
I like clean lines and simple designs, but it pops using the colors scheme (one or two colors) on the website.
I provide life and health coaching virtually and in person. My services include: Dietary Signal Screening, Sensitivity Clearing Review, Wellness Coaching, Life Coaching. Life and Health Assessments, and I sell foundational health products and specialized nutrition. Use colors that represent healing and trust.
Target Market(s)
Women for the ages of 30 - 60
Industry/Entity Type
Health
Contact Information for Business Card
Tessa Rosalind Kimble
Life and Wellness Coach
tessa@coachtrk.net
www.brightpathwell.net
555-217-8364
Health is not an event it's a lifestyle (tag line or if you have a better tag line)

```html
<!DOCTYPE html>
<html lang="en">
<head>
<meta charset="utf-8">
<title>Tessa Rosalind Kimble — Business Card</title>
<link href="https://fonts.googleapis.com/css2?family=Source+Sans+3:ital,wght@0,400;1,400&display=swap" rel="stylesheet">
<style>
  :root {
    --backdrop: #d3d4d7;
    --card: #ffffff;
    --ink: #111111;
    --gold: #b8913a;
  }
  * { margin: 0; padding: 0; box-sizing: border-box; }
  html, body {
    width: 1200px;
    height: 960px;
    overflow: hidden;
    background: var(--backdrop);
    font-family: "Source Sans 3", "Helvetica Neue", Arial, sans-serif;
  }
  .card {
    position: absolute;
    left: 75px;
    top: 180px;
    width: 1050px;
    height: 600px;
    background: var(--card);
  }
  .identity {
    position: absolute;
    right: 53px;
    top: 42px;
    text-align: right;
  }
  .identity__name {
    font-size: 31px;
    line-height: 32px;
    color: var(--ink);
    font-weight: 400;
  }
  .identity__title {
    font-size: 27px;
    line-height: 30px;
    color: var(--gold);
    font-style: italic;
  }
  .rule {
    position: absolute;
    top: 298px;
    height: 3px;
    background: var(--ink);
  }
  .rule--lead { left: 0; width: 128px; }
  .rule--trail { left: 678px; width: 124px; }
  .tagline {
    position: absolute;
    left: 137px;
    top: 280px;
    font-size: 26px;
    line-height: 34px;
    letter-spacing: 2.6px;
    color: var(--gold);
    white-space: nowrap;
  }
  .wordmark {
    position: absolute;
    left: 808px;
    top: 237px;
    font-size: 76px;
    line-height: 76px;
    color: var(--ink);
    font-weight: 400;
    letter-spacing: 6px;
  }
  .contact {
    position: absolute;
    left: 52px;
    top: 486px;
    font-size: 26px;
    line-height: 25px;
    color: var(--ink);
    list-style: none;
  }
</style>
</head>
<body>
  <main class="card">
    <header class="identity">
      <h1 class="identity__name">Tessa Rosalind Kimble</h1>
      <p class="identity__title">Life and Wellness Coach</p>
    </header>

    <div class="rule rule--lead"></div>
    <p class="tagline">Health is not an event it's a lifestyle</p>
    <div class="rule rule--trail"></div>
    <div class="wordmark">TRK</div>

    <ul class="contact">
      <li>555-217-8364</li>
      <li>www.brightpathwell.net</li>
      <li>tessa@coachtrk.net</li>
    </ul>
  </main>
</body>
</html>
```